Business Card & Stationery for a Consulting Firm
Brivaro Consulting
Business Card & Stationery for a Consulting Firm - Consulting
Creative Brief
Professional
Kusumadewi Pramulyanto
Senior Consultant
Graha 4 Suite-M, Level 11 Jl Raya Pelangi Kav. 17-18 Taman Niaga Raya (TNR) Jakarta 12760
kusumadewi@brivaroconsulting-example.com
www.brivaroconsulting-example.com
Kusumadewi Kusumadewi
Dear All Designers, On the address, please omit the line "Taman Niaga Rayaa (TNR) and add Twitter: @brivaroconsulting and Facebook: Brivaro Consulting. Thank you

```html
<!DOCTYPE html>
<html lang="en">
<head>
<meta charset="utf-8">
<title>Brivaro Consulting – Stationery</title>
<link href="https://fonts.googleapis.com/css2?family=Roboto:wght@400;700&display=swap" rel="stylesheet">
<style>
  :root{
    --navy:#1f3a78;
    --grey:#9a9a9a;
    --ink:#3a3a3a;
    --paper:#ffffff;
    --bg:#eeeeee;
    --edge:#dcdcdc;
  }
  *{box-sizing:border-box;margin:0;padding:0}
  html,body{width:1200px;height:937px;overflow:hidden;background:var(--bg);font-family:"Roboto",Arial,sans-serif;color:var(--ink)}
  .canvas{position:relative;width:1200px;height:937px}
  .sheet{position:absolute;background:var(--paper);border:1px solid var(--edge);overflow:hidden}

  /* brand name */
  .brand{display:flex;align-items:center;gap:.35em;font-size:var(--s,20px)}
  .brand-dot{width:.55em;height:.55em;border-radius:50%;background:var(--navy);flex:none}
  .brand-name{font-weight:700;color:var(--navy);line-height:1.02;white-space:nowrap}

  /* footer band */
  .band{position:absolute;left:0;right:0;bottom:0;height:var(--h,16px);display:flex;align-items:flex-end}
  .band-blue{height:100%;width:var(--w,62%);background:var(--navy);border-top-right-radius:var(--h,16px) 100%;color:#fff;font-size:calc(var(--h,16px)*.5);display:flex;align-items:center;padding-left:1.2em;letter-spacing:.04em;white-space:nowrap}
  .band-grey{flex:1;height:40%;background:var(--grey)}

  /* letterhead */
  .letterhead{left:182px;top:63px;width:388px;height:552px}
  .letterhead .brand{position:absolute;left:34px;top:44px;--s:20px}
  .lh-contact{position:absolute;right:26px;top:34px;width:160px;text-align:right;font-size:6px;line-height:1.45;color:var(--ink);font-style:normal}
  .lh-body{position:absolute;left:34px;top:128px;width:320px;font-size:6.2px;line-height:1.55}
  .lh-body p{margin-bottom:8px}
  .lh-sign{margin-top:26px}

  /* folder */
  .folder{left:633px;top:38px;width:390px;height:577px}
  .folder .brand{position:absolute;left:50%;top:255px;transform:translateX(-50%);--s:36px}
  .folder .band{--h:22px;--w:66%}

  /* business cards */
  .card{width:182px;height:92px;left:46px}
  .card-front{top:666px}
  .card-back{top:785px}
  .card .band{--h:8px;--w:56%}
  .card-front .brand{position:absolute;right:10px;top:12px;--s:10px}
  .card-name{position:absolute;left:10px;top:12px;font-size:6px;font-weight:700;color:var(--navy);white-space:nowrap}
  .card-role{position:absolute;left:10px;top:20px;font-size:4.6px}
  .card-lines{position:absolute;right:10px;top:44px;width:110px;text-align:right;font-size:4.3px;line-height:1.45}
  .card-back .brand{position:absolute;left:10px;top:14px;--s:9px}
  .card-back .card-lines{top:16px;width:100px;font-size:4px}

  /* envelopes */
  .env-front{left:268px;top:676px;width:431px;height:205px}
  .env-front .brand{position:absolute;left:24px;top:28px;--s:22px}
  .env-front .band{--h:16px;--w:48%}
  .env-back{left:739px;top:676px;width:431px;height:205px}
  .env-flap{position:absolute;left:0;top:0;width:100%;height:92px}
  .env-url{position:absolute;left:0;right:0;top:26px;text-align:center;color:#fff;font-size:14px;letter-spacing:.18em}
</style>
</head>
<body>
<main class="canvas">

  <section class="sheet letterhead" aria-label="Letterhead">
    <div class="brand">
      <span class="brand-dot"></span>
      <span class="brand-name">Brivaro<br>Consulting</span>
    </div>
    <address class="lh-contact">
      Graha 4 Suite-M, Level 11<br>
      Jl Raya Pelangi Kav. 17-18<br>
      Jakarta 12760<br>
      +62 21 5550 1234<br>
      kusumadewi@brivaroconsulting-example.com
    </address>
    <div class="lh-body">
      <p>July 4, 2014</p>
      <p>Dear Client,<br>PT Sample Company<br>Jl Contoh No. 1, Jakarta</p>
      <p>Thank you for the opportunity to present our proposal. We look forward to supporting your team with clear strategy, careful analysis and practical guidance for lasting business growth.</p>
      <p>Our consultants will review current processes, identify key opportunities and agree measurable targets with you before any work begins.</p>
      <p>Please contact us at any time should you have questions about the scope, timeline or fees outlined in this letter.</p>
      <p>Sincerely,</p>
      <p class="lh-sign">Kusumadewi Pramulyanto<br>Senior Consultant</p>
    </div>
    <div class="band" style="--h:14px;--w:62%">
      <div class="band-blue">www.brivaroconsulting-example.com</div>
      <div class="band-grey"></div>
    </div>
  </section>

  <section class="sheet folder" aria-label="Presentation folder">
    <div class="brand">
      <span class="brand-dot"></span>
      <span class="brand-name">Brivaro<br>Consulting</span>
    </div>
    <div class="band">
      <div class="band-blue">www.brivaroconsulting-example.com</div>
      <div class="band-grey"></div>
    </div>
  </section>

  <section class="sheet card card-front" aria-label="Business card front">
    <div class="card-name">Kusumadewi Pramulyanto</div>
    <div class="card-role">Senior Consultant</div>
    <div class="brand">
      <span class="brand-name">Brivaro<br>Consulting</span>
    </div>
    <div class="card-lines">
      Graha 4 Suite-M, Level 11<br>
      Jl Raya Pelangi Kav. 17-18<br>
      Jakarta 12760<br>
      +62 21 5550 1234
    </div>
    <div class="band"><div class="band-blue"></div><div class="band-grey"></div></div>
  </section>

  <section class="sheet card card-back" aria-label="Business card back">
    <div class="brand">
      <span class="brand-name">Brivaro<br>Consulting</span>
    </div>
    <div class="card-lines">
      kusumadewi@brivaroconsulting-example.com<br>
      www.brivaroconsulting-example.com<br>
      Twitter: @brivaroconsulting<br>
      Facebook: Brivaro Consulting
    </div>
    <div class="band"><div class="band-blue"></div><div class="band-grey"></div></div>
  </section>

  <section class="sheet env-front" aria-label="Envelope front">
    <div class="brand">
      <span class="brand-dot"></span>
      <span class="brand-name">Brivaro<br>Consulting</span>
    </div>
    <div class="band">
      <div class="band-blue">www.brivaroconsulting-example.com</div>
      <div class="band-grey"></div>
    </div>
  </section>

  <section class="sheet env-back" aria-label="Envelope back">
    <svg class="env-flap" viewBox="0 0 431 92" preserveAspectRatio="none" aria-hidden="true">
      <path d="M0 0H431V70Q431 84 410 86L21 86Q0 84 0 70Z" fill="#1f3a78"/>
    </svg>
    <div class="env-url">www.brivaroconsulting-example.com</div>
  </section>

</main>
</body>
</html>
```